Movie Genre Illustrations

We need a dozen of illustrations for movie genres for an online video store.

The dimensions for the images is 650 x 240.
The images will be placed on a dark background.

The images should be a mixture of some unique font displaying the 'attitude' of the genre, with complementing background image.

An example for "Kids"
a colourful balloon background with a childish font.
An example for "Science Fiction"
a starscape background with some futuristic font.

The categories are as below, the text in quotes is the danish text and should be the text shown in the illustrations, the preceding translations are added for your convenience:

Action "Action"
Comedy "Komedie"
Science Fiction "Science Fiction"
Thriller "Thriller"
Drama "Drama"
Romance "Romantik"
Animation "Animation"
Kids "Børnefilm"
Danish Movies "Danske film" // if you don't know much about Denmark you can skip this one.
War Movies "Krigsfilm"
Horror "Gyser"
Adventure "Eventyr"
Crime "Krimi"
Stand-up "Stand-up og satire"
Youth "Ungdom"
Documentary "Dokumentar"
Martial Arts (kung fu movies) "Kampsport"

For inspiration look to some of the feature banners in the Qorvia store promoting genre specific content (more examples in the App section of the Qorvia store).

important, these images will be presented on a TV, please avoid using large white areas, and make sure the white you use is #f1f1f1 instead of #fff.

There are two designs right now, both of them are way too noisy, there are way too many elements, and the backgrounds are crowded, please simplify things, this is for a scandinavian audience, simplicity is key (think brumlo).

Danish TV users

Movie

```html
<!DOCTYPE html>
<html lang="da">
<head>
<meta charset="utf-8">
<title>Genre banners – Eventyr, Krigsfilm, Thriller</title>
<link rel="stylesheet" href="https://fonts.googleapis.com/css2?family=Michroma&family=Russo+One&family=Teko:wght@500&display=swap">
<style>
  :root {
    --frame: #0b0b0b;
    --board: #f1f1f1;
    --board-shade: rgba(0, 0, 0, 0.28);
    --stone-light: #8a7a58;
    --stone-mid: #5e5138;
    --stone-dark: #2a2417;
    --scale-light: #6b5a45;
    --scale-dark: #120d08;
    --scale-ember: #8a3a14;
    --steel-light: #e6e6e2;
    --steel-mid: #9a9a96;
    --steel-dark: #55544f;
    --brass: #b59a3c;
    --night-deep: #04103f;
    --night-mid: #0c2fa0;
    --night-glow: #2c6fe8;
    --ice: #6fd2ff;
  }

  * { margin: 0; padding: 0; box-sizing: border-box; }

  html, body {
    width: 1200px;
    height: 900px;
    overflow: hidden;
  }

  body {
    position: relative;
    background: var(--frame);
  }

  .presentation-board {
    position: absolute;
    left: 12px;
    top: 12px;
    width: 1176px;
    height: 876px;
    background: var(--board);
    box-shadow: inset 0 0 28px 6px var(--board-shade);
  }

  .genre-banner {
    position: absolute;
    left: 275px;
    width: 650px;
    height: 240px;
    overflow: hidden;
  }

  .genre-banner--adventure { top: 76px; }
  .genre-banner--war { top: 331px; }
  .genre-banner--thriller { top: 584px; }

  .banner-backdrop {
    position: absolute;
    inset: 0;
  }

  .genre-banner--adventure .banner-backdrop {
    background:
      radial-gradient(ellipse at 50% 50%, var(--stone-light) 0%, var(--stone-mid) 55%, var(--stone-dark) 100%);
  }

  .genre-banner--war .banner-backdrop {
    background:
      radial-gradient(ellipse 40% 60% at 90% 75%, var(--scale-ember) 0%, transparent 70%),
      radial-gradient(ellipse at 50% 40%, var(--scale-light) 0%, #3b2f22 55%, var(--scale-dark) 100%);
  }

  .genre-banner--thriller .banner-backdrop {
    background:
      radial-gradient(ellipse 60% 45% at 50% 62%, var(--night-glow) 0%, transparent 75%),
      linear-gradient(180deg, var(--night-deep) 0%, var(--night-mid) 60%, #1747c8 100%);
  }

  .genre-title {
    position: absolute;
    left: 0;
    width: 100%;
    text-align: center;
    white-space: nowrap;
    -webkit-background-clip: text;
    background-clip: text;
    color: transparent;
  }

  .genre-banner--adventure .genre-title {
    top: 58px;
    font-family: "Michroma", sans-serif;
    font-size: 80px;
    line-height: 1.3;
    letter-spacing: -1px;
    background-image: linear-gradient(180deg, var(--steel-light) 0%, var(--steel-mid) 50%, var(--steel-dark) 100%);
    filter: drop-shadow(4px 4px 0 var(--brass)) drop-shadow(4px 6px 6px rgba(0, 0, 0, 0.7));
  }

  .genre-banner--war .genre-title {
    top: 76px;
    font-family: "Russo One", sans-serif;
    font-size: 70px;
    line-height: 1.3;
    letter-spacing: 3px;
    background-image: linear-gradient(180deg, var(--steel-light) 0%, #8d8a80 55%, #4a463c 100%);
    filter: drop-shadow(2px 3px 0 var(--brass)) drop-shadow(2px 4px 6px rgba(0, 0, 0, 0.8));
  }

  .genre-banner--thriller .genre-title,
  .genre-banner--thriller .title-reflection {
    font-family: "Teko", sans-serif;
    font-weight: 500;
    font-size: 112px;
    line-height: 1;
    letter-spacing: 12px;
  }

  .genre-banner--thriller .genre-title {
    top: 66px;
    background-image: linear-gradient(180deg, var(--ice) 0%, #1d6fd6 35%, #030a22 60%, #0a1c5c 100%);
    filter: drop-shadow(0 0 6px rgba(60, 150, 255, 0.6));
  }

  .title-reflection {
    position: absolute;
    left: 0;
    top: 152px;
    width: 100%;
    text-align: center;
    white-space: nowrap;
    color: #0a2a8a;
    transform: scaleY(-1);
    opacity: 0.55;
  }

  .horizon-line {
    position: absolute;
    left: 0;
    top: 145px;
    width: 100%;
    height: 1px;
    background: linear-gradient(90deg, transparent, var(--ice), transparent);
    opacity: 0.6;
  }
</style>
</head>
<body>
  <main class="presentation-board">
    <section class="genre-banner genre-banner--adventure">
      <div class="banner-backdrop" role="img" aria-label="Weathered rock surface in ochre and brown tones"></div>
      <h2 class="genre-title">EVENTYR</h2>
    </section>

    <section class="genre-banner genre-banner--war">
      <div class="banner-backdrop" role="img" aria-label="Dark armour-scale texture with a burnt hole and an orange glow"></div>
      <h2 class="genre-title">KRIGSFILM</h2>
    </section>

    <section class="genre-banner genre-banner--thriller">
      <div class="banner-backdrop" role="img" aria-label="Deep blue background with sweeping light streaks"></div>
      <h2 class="genre-title">THRILLER</h2>
      <div class="horizon-line"></div>
      <div class="title-reflection" aria-hidden="true">THRILLER</div>
    </section>
  </main>
</body>
</html>
```